SMS wordpress page 1 pager with mobile phone messaging graphics

Create a one page landing page. The page will have 2 mobile phones on the right sending and receiving messages. The messages will be according to the videos below. On the left each of the commands should highlight and then show the command on the phones on the right. You can get the information for commands from sms.pellomark.example. Place a button with link at the bottom saying: Open your free bank account with PelloMark link: pellomark.example/register. Top left please put the header: Receive $5 TOKAS free when you signup. Receive $5 TOKAS free when you refer you create or refer an account for your friends and family. Please use the color scheme from the logos below. Text me at 5203318867 with your whatsapp number (with country code) and I can sign you up and you can test the service.
users 18-55

```html
<!DOCTYPE html>
<html lang="en">
<head>
<meta charset="utf-8">
<title>PelloMark – SMS Banking Landing Page</title>
<link rel="stylesheet" href="https://fonts.googleapis.com/css2?family=Poppins:wght@300;400;500;600;700;800&display=swap">
<style>
  :root{
    --navy:#0f1130;
    --navy-soft:#1b1d3f;
    --cyan:#1ad3e8;
    --blue:#1f9bf2;
    --blue-deep:#1780e0;
    --coral:#f4675c;
    --coral-soft:#f7837a;
    --ink:#15162b;
    --grey:#7b7f92;
    --page:#f6f9fd;
    --tint:#e7f0fc;
    --white:#ffffff;
    --avatar:#5d6fd8;
  }
  *{box-sizing:border-box;margin:0;padding:0}
  html,body{width:1200px;height:1200px;overflow:hidden;background:var(--white)}
  body{font-family:"Poppins",sans-serif;color:var(--ink);position:relative}

  .page{position:absolute;top:23px;width:602px;background:var(--page);transform:scale(0.625);transform-origin:0 0;box-shadow:0 6px 30px rgba(15,17,48,.12);overflow:hidden}
  .page--home{left:204px;height:1843px}
  .page--guide{left:632px;height:1658px}
  .abs{position:absolute}

  /* header */
  .topbar{left:0;top:0;width:602px;height:55px;background:var(--navy)}
  .topbar__mark{left:19px;top:12px;width:30px;height:30px;border:2px solid var(--cyan);border-radius:50%}
  .search{left:240px;top:19px;width:180px;height:18px;border:1px solid #fff;border-radius:9px;color:#fff;font-size:5.5px;line-height:16px;padding-left:12px}
  .search__btn{right:-1px;top:-1px;width:52px;height:18px;background:var(--cyan);border-radius:9px;color:#fff;font-size:5.5px;text-align:center;line-height:18px}
  .login{left:444px;top:19px;width:77px;height:18px;border:1px solid var(--cyan);border-radius:9px;color:#fff;font-size:5.5px;text-align:center;line-height:16px}

  .sidebar{left:0;top:55px;width:64px;height:263px;background:var(--navy)}
  .sidebar__item{width:64px;height:31.5px;border-bottom:1px solid rgba(255,255,255,.08);display:flex;align-items:center;justify-content:center}
  .sidebar__item--active{background:var(--cyan)}

  /* hero */
  .hero{left:0;top:55px;width:602px;height:323px}
  .brand{display:flex;align-items:center;gap:9px;font-size:22px;font-weight:400;color:var(--ink)}
  .brand__dot{width:36px;height:36px;border:2.5px solid var(--cyan);border-radius:50%}
  .hero__title{left:80px;top:145px;font-size:27px;font-weight:700;line-height:31px;color:var(--ink)}
  .hero__sub{left:80px;top:210px;font-size:19px;font-weight:400}
  .field{left:80px;top:250px;width:196px;height:30px;border:1px solid #c9ccd6;background:#fff;font-size:8px;color:var(--grey);padding:9px 14px}
  .pill{border-radius:12px;color:#fff;font-size:7.5px;text-align:center}
  .pill--coral{background:var(--coral)}
  .fineprint{font-size:5.5px;color:var(--grey);line-height:10px}

  /* sections */
  .section{left:0;width:602px}
  .h2{font-size:21px;font-weight:700;line-height:25px}
  .body-s{font-size:7.5px;line-height:11px;color:var(--grey)}
  .placeholder{position:absolute}

  .why{top:668px;height:227px;background:linear-gradient(120deg,#2aa4f3,#1b8ee8)}
  .offer{top:895px;height:143px;background:var(--coral)}
  .offer__text{font-size:15px;line-height:21px;color:#fff;font-weight:400}
  .offer__text b{font-weight:600}
  .welcome{top:1038px;height:238px;background:var(--navy);overflow:hidden}
  .center{width:602px;text-align:center}

  .howto{top:1276px;height:327px;background:var(--page)}
  .tinted{background:var(--tint)}
  .plain{background:var(--white)}

  .step-num{width:29px;height:29px;border:1px solid var(--coral);border-radius:50%;color:var(--coral);font-size:13px;text-align:center;line-height:27px}
  .step-title{font-size:17.5px;font-weight:600;color:var(--ink);line-height:21px}
  .step-body{font-size:11.5px;line-height:21px;color:var(--ink);font-weight:400}
  .step-body em{font-style:normal;color:var(--coral)}

  /* phone mock */
  .phone{position:absolute;width:151px;background:#fff;border-radius:13px 13px 0 0;box-shadow:0 2px 14px rgba(20,30,80,.16);overflow:hidden;padding:7px 8px 0}
  .phone__status{display:flex;justify-content:space-between;align-items:center;height:8px}
  .phone__time{background:#e8443a;color:#fff;font-size:3.5px;border-radius:3px;padding:0 3px;line-height:5px}
  .phone__signal{font-size:3.5px;color:#555}
  .phone__head{display:flex;justify-content:space-between;font-size:5px;color:#222;padding:4px 2px 5px;border-bottom:1px solid #ddd}
  .msg{display:flex;gap:5px;align-items:flex-start;margin:6px 0 0 3px}
  .msg__avatar{width:9px;height:9px;border-radius:50%;background:var(--avatar);flex:none;margin-top:6px}
  .msg__text{font-size:4.3px;line-height:5.6px;color:#222;width:84px}
  .msg__meta{font-size:3.2px;color:#999;margin-top:1px}
  .sent{text-align:right;font-size:4.3px;color:var(--blue-deep);margin:6px 8px 0 0}
  .sent small{display:block;font-size:3.2px;color:#999}
  .phone__input{display:flex;gap:4px;align-items:center;font-size:4px;color:#888;border-top:1px solid #eee;margin-top:8px;padding:4px 2px}
  .keys{display:flex;justify-content:space-between;font-size:5px;color:#333;padding:3px 2px}
  .keys span{width:11px;height:11px;border:1px solid #ddd;border-radius:2px;text-align:center;line-height:10px}
  .link{color:var(--blue-deep);text-decoration:underline}

  /* CTA + footer */
  .cta{top:1288px;height:175px;background:var(--navy-soft)}
  .cta__btn{left:198px;top:93px;width:207px;height:30px;background:var(--cyan);color:var(--navy);font-size:13.5px;font-weight:500;text-align:center;line-height:28px;border:1px dashed var(--navy)}
  .footer{top:1463px;height:145px;background:#fff}
  .social{width:15px;height:15px;border:1px solid #9aa0b0;border-radius:50%}
  .footnav{display:flex;justify-content:center;gap:16px;font-size:6.5px;color:#333}
  .copyright{top:1608px;height:50px;background:var(--tint)}
</style>
</head>
<body>

<!-- ============ HOME PAGE ============ -->
<section class="page page--home">

  <header class="abs topbar">
    <div class="abs topbar__mark"></div>
    <div class="abs search">Search Here...<span class="abs search__btn">Search</span></div>
    <div class="abs login">Log in or Sign up</div>
  </header>

  <div class="abs hero">
    <svg class="abs" style="left:0;top:0" width="602" height="323" viewBox="0 0 602 323">
      <path d="M410 0H602V305C540 300 470 290 430 240C400 200 440 160 420 110C405 70 395 30 410 0Z" fill="#1f9bf2"/>
    </svg>
    <div class="placeholder" role="img" aria-label="Photo of two excited friends looking at a smartphone" style="left:315px;top:23px;width:260px;height:260px;border-radius:50%;background:radial-gradient(circle at 45% 40%,#f1a772,#2c8a96 55%,#e08d2a)"></div>
    <div class="abs brand" style="left:80px;top:90px"><span class="brand__dot"></span>PelloMark</div>
    <h1 class="abs hero__title">Bring Some<br>Cryptocurrency</h1>
    <p class="abs hero__sub">Into Your Life Today</p>
    <div class="abs field">Your E-mail*</div>
    <div class="abs pill pill--coral" style="left:80px;top:235px;width:101px;height:21px;line-height:21px;transform:translateY(55px)">Get Early Access</div>
    <p class="abs fineprint" style="left:80px;top:322px">Your privacy is of the utmost importance to us.<br>We will never share your information.</p>
  </div>

  <nav class="abs sidebar">
    <div class="sidebar__item sidebar__item--active"><svg width="14" height="14" viewBox="0 0 14 14" fill="none" stroke="#0f1130" stroke-width="1.2"><path d="M2 7L7 2L12 7V12H2Z"/></svg></div>
    <div class="sidebar__item"><svg width="14" height="14" viewBox="0 0 14 14" fill="none" stroke="#fff" stroke-width="1"><circle cx="7" cy="6" r="4"/><path d="M3 12H11"/></svg></div>
    <div class="sidebar__item"><svg width="14" height="14" viewBox="0 0 14 14" fill="none" stroke="#fff" stroke-width="1"><rect x="2" y="3" width="10" height="8" rx="1"/><path d="M2 6H12"/></svg></div>
    <div class="sidebar__item"><svg width="14" height="14" viewBox="0 0 14 14" fill="none" stroke="#fff" stroke-width="1"><path d="M7 1L8.6 5.2H13L9.5 8L10.8 12.5L7 9.8L3.2 12.5L4.5 8L1 5.2H5.4Z"/></svg></div>
    <div class="sidebar__item"><svg width="14" height="14" viewBox="0 0 14 14" fill="none" stroke="#fff" stroke-width="1"><path d="M1 2H3L5 9H11L12.5 4H4"/><circle cx="5.5" cy="11.5" r="1"/><circle cx="10.5" cy="11.5" r="1"/></svg></div>
    <div class="sidebar__item"><svg width="14" height="14" viewBox="0 0 14 14" fill="none" stroke="#fff" stroke-width="1"><path d="M1 5L7 2L13 5L7 8Z"/><path d="M4 6.5V10C6 11.5 8 11.5 10 10V6.5"/></svg></div>
    <div class="sidebar__item"><svg width="14" height="14" viewBox="0 0 14 14" fill="none" stroke="#fff" stroke-width="1"><circle cx="7" cy="5" r="3"/><path d="M2 13C3 9 11 9 12 13"/></svg></div>
  </nav>

  <!-- Debit card -->
  <div class="abs section" style="top:378px;height:290px;background:#fff">
    <div class="placeholder" role="img" aria-label="Illustration of a blue debit card in front of blue circles" style="left:95px;top:37px;width:160px;height:230px;border-radius:80px;background:radial-gradient(circle at 50% 35%,#2a8ef0,#b9d6f5 75%)"></div>
    <svg class="abs" style="left:490px;top:12px" width="48" height="48" viewBox="0 0 48 48"><circle cx="24" cy="24" r="21" fill="none" stroke="#c9d6ee"/><circle cx="25" cy="23" r="14" fill="#1f9bf2"/><circle cx="13" cy="36" r="4" fill="#1780e0"/></svg>
    <h2 class="abs h2" style="left:298px;top:73px">Your Debit Card</h2>
    <p class="abs body-s" style="left:298px;top:110px;width:225px">Because we are a payments system owned by our members - including you.</p>
    <p class="abs body-s" style="left:298px;top:143px;width:225px">We reward you when you spend, save, or exchange your money using your exclusive debit card. No matter your approach to money- we stand united!</p>
    <div class="abs pill pill--coral" style="left:298px;top:193px;width:72px;height:22px;line-height:22px">Read More</div>
  </div>

  <!-- Why join -->
  <div class="abs section why">
    <div class="placeholder" role="img" aria-label="Smartphone showing a crypto wallet app" style="left:395px;top:-15px;width:120px;height:225px;border-radius:18px;background:linear-gradient(180deg,#2f3357 0%,#2f3357 35%,#ffffff 36%);transform:rotate(-16deg);box-shadow:0 6px 18px rgba(0,0,0,.2)"></div>
    <h2 class="abs h2" style="left:80px;top:42px;color:#fff">Why Join<br>PelloMark?</h2>
    <p class="abs" style="left:80px;top:107px;width:218px;font-size:7.5px;line-height:11.3px;color:#fff">Because we are a decentralized banking system owned by our members - including you. We reward you when you exchange, save, or spend your cryptocurrencies using your exclusive debit card. No matter your approach to crypto - we stand united!</p>
    <div class="abs pill pill--coral" style="left:80px;top:184px;width:72px;height:21px;line-height:21px">Read More</div>
  </div>

  <!-- Offer band -->
  <div class="abs section offer">
    <p class="abs offer__text" style="left:80px;top:29px;width:175px"><b>Receive $5 TOKAS</b> free when you signup</p>
    <div class="abs" style="left:268px;top:24px;width:1px;height:97px;background:rgba(255,255,255,.55)"></div>
    <p class="abs offer__text" style="left:304px;top:29px;width:220px"><b>Receive $5 TOKAS</b> free when you refer you create or refer an account for your friends and family</p>
  </div>

  <!-- Welcome -->
  <div class="abs section welcome">
    <svg class="abs" style="left:0;top:0" width="602" height="238" viewBox="0 0 602 238">
      <path d="M560 0H602V58C575 50 560 25 560 0Z" fill="#1f9bf2"/>
      <path d="M0 148C25 148 40 175 30 200C60 210 70 225 72 238H0Z" fill="#1f9bf2"/>
      <path d="M0 175C25 178 55 205 72 238H60C45 212 25 195 0 190Z" fill="#e9f2fd"/>
    </svg>
    <p class="abs center" style="top:35px;font-size:20px;font-weight:700;color:#fff;letter-spacing:.3px">WELCOME TO PELLOMARK.</p>
    <p class="abs center" style="top:60px;font-size:18px;font-weight:400;color:var(--cyan)">MONEY FOR EVERYONE.</p>
    <div class="abs" style="left:80px;top:107px;width:440px;height:1px;background:rgba(255,255,255,.3)"></div>
    <p class="abs center" style="top:128px;font-size:16.5px;font-weight:500;color:var(--coral)">How do I open a new account?</p>
    <p class="abs center" style="top:158px;font-size:11.5px;line-height:21px;color:#fff">Have a friend with a PelloMark account create one for you,<br>or text our founder: send 'Hello' to <span style="color:var(--cyan);font-weight:600">+1-555-014-2288</span></p>
  </div>

  <!-- How to use -->
  <div class="abs section howto">
    <h2 class="abs center" style="top:24px;font-size:20px;font-weight:700">How to use PelloMark Mobile</h2>
    <div class="abs" style="left:225px;top:59px;width:152px;height:2px;background:var(--blue)"></div>
    <div class="abs step-num" style="left:102px;top:111px">01</div>
    <h3 class="abs step-title" style="left:102px;top:154px">Create New Accounts</h3>
    <p class="abs step-body" style="left:102px;top:184px;width:260px">To create an account for a new person enter the text message (for example):<br>create <em>+123456 78910</em></p>
    <div class="phone" style="left:370px;top:107px;height:220px">
      <div class="phone__status"><span class="phone__time">15:12</span><span class="phone__signal">LTE ▮</span></div>
      <div class="phone__head"><span>‹</span><span>(555) 010-4471</span><span>☏ ⋯</span></div>
      <div class="msg"><span class="msg__avatar"></span><div class="msg__text">PelloMark has changed your PIN. If you think you have received this message in error, please contact us immediately.<div class="msg__meta">(555) 010-4471 · 15:10</div></div></div>
      <div class="sent">Create <span class="link">5203318867</span><small>15:12</small></div>
      <div class="msg"><span class="msg__avatar"></span><div class="msg__text">You requested PelloMark to create a new account. Please send your PIN to complete your transaction.<div class="msg__meta">(555) 010-4471 · 15:12</div></div></div>
      <div class="phone__input">▢ ▣ |Type a message</div>
      <div class="keys"><span>1</span><span>2</span><span>3</span><span>4</span><span>5</span><span>6</span><span>7</span><span>8</span><span>9</span><span>0</span></div>
      <div class="keys"><span>-</span><span>/</span><span>:</span><span>;</span><span>(</span><span>)</span><span>$</span><span>&amp;</span><span>@</span><span>"</span></div>
    </div>
  </div>

  <div class="abs section tinted" style="top:1603px;height:240px">
    <div class="phone" style="left:81px;top:27px;height:215px">
      <div class="phone__status"><span class="phone__time">15:14</span><span class="phone__signal">LTE ▮</span></div>
      <div class="phone__head"><span>‹</span><span>(555) 010-4471</span><span>☏ ⋯</span></div>
      <div class="msg" style="margin-top:2px"><span class="msg__avatar" style="visibility:hidden"></span><div class="msg__text">notified when their account has been created</div></div>
      <div class="msg"><span class="msg__avatar"></span><div class="msg__text">You have received a payment of TOKAS, amount: 10 from PelloMark.<div class="msg__meta">(555) 010-4471 · 15:12</div></div></div>
      <div class="sent">Send 5 TOKAS <span class="link">5203318867</span><small>15:13</small></div>
      <div class="msg"><span class="msg__avatar"></span><div class="msg__text">You requested PelloMark SEND MONEY. Please send your PIN to complete your transaction.<div class="msg__meta">(555) 010-4471 · 15:13</div></div></div>
      <div class="phone__input">▢ ▣ |Type a message</div>
      <div class="keys"><span>1</span><span>2</span><span>3</span><span>4</span><span>5</span><span>6</span><span>7</span><span>8</span><span>9</span><span>0</span></div>
      <div class="keys"><span>-</span><span>/</span><span>:</span><span>;</span><span>(</span><span>)</span><span>$</span><span>&amp;</span><span>@</span><span>"</span></div>
    </div>
    <div class="abs step-num" style="left:274px;top:30px">02</div>
    <h3 class="abs step-title" style="left:274px;top:72px">Send TOKAS</h3>
    <p class="abs step-body" style="left:274px;top:103px;width:250px">To send money to someone enter the text message (for example):<br>'Hello' to send $1 to <em>+123456 78910</em></p>
  </div>
</section>

<!-- ============ GUIDE PAGE ============ -->
<section class="page page--guide">

  <div class="abs section plain" style="top:0;height:263px">
    <div class="abs step-num" style="left:102px;top:50px">03</div>
    <h3 class="abs step-title" style="left:102px;top:92px">See Your Balances</h3>
    <p class="abs step-body" style="left:102px;top:124px;width:250px">o see your account balances send the text message: <em>balances</em></p>
    <div class="phone" style="left:370px;top:46px;height:217px">
      <div class="phone__status"><span class="phone__time">15:14</span><span class="phone__signal">4G ▮</span></div>
      <div class="phone__head"><span>‹</span><span>(555) 010-4471</span><span>☏ ⋯</span></div>
      <div class="msg"><span class="msg__avatar"></span><div class="msg__text">Welcome. Please open an account with PelloMark to access our SMS interface!<div class="msg__meta">(555) 010-4471 · Aug 18, 15:08</div></div></div>
      <div class="sent">Balances</div>
      <div class="sent" style="margin-top:4px">Hello<small>15:02</small></div>
      <div class="msg"><span class="msg__avatar" style="visibility:hidden"></span><div class="msg__text">Welcome to PelloMark! Invite your friends and family by creating an account for them and receive 10 TOKAS. Your PIN is: 46153023<br><br>Change your PIN, send TOKAS, and see your balances via text messages! For details see <span class="link">sms.pellomark.example</span>. Enter "CHANGE PIN to &lt;your new PIN&gt;" now!</div></div>
    </div>
  </div>

  <div class="abs section tinted" style="top:263px;height:247px">
    <div class="phone" style="left:82px;top:29px;height:218px">
      <div class="phone__status"><span class="phone__time">15:10</span><span class="phone__signal">LTE ▮</span></div>
      <div class="phone__head"><span>‹</span><span>(555) 010-4471</span><span>☏ ⋯</span></div>
      <div class="msg"><span class="msg__avatar"></span><div class="msg__text">Your account can hold multiple currency denominations. Your balances are:<br>&nbsp;TOKAS 10<div class="msg__meta">(555) 010-4471 · Jul 27, 08:19</div></div></div>
      <div class="sent">Change pin to <span class="link">12345678</span><small>15:10</small></div>
      <div class="msg"><span class="msg__avatar"></span><div class="msg__text">You requested PelloMark CHANGE PIN. Please send your current PIN to complete your transaction.<div class="msg__meta">(555) 010-4471 · 15:10</div></div></div>
      <div class="phone__input">▢ ▣ |Type a message</div>
      <div class="keys"><span>1</span><span>2</span><span>3</span><span>4</span><span>5</span><span>6</span><span>7</span><span>8</span><span>9</span><span>0</span></div>
      <div class="keys"><span>-</span><span>/</span><span>:</span><span>;</span><span>(</span><span>)</span><span>$</span><span>&amp;</span><span>@</span><span>"</span></div>
    </div>
    <div class="abs step-num" style="left:273px;top:34px">04</div>
    <h3 class="abs step-title" style="left:273px;top:77px">Change your PIN</h3>
    <p class="abs step-body" style="left:273px;top:108px;width:250px">To change your PIN use the text message (for example): change pin to <em>12345678</em></p>
  </div>

  <div class="abs section plain" style="top:510px;height:266px">
    <div class="abs step-num" style="left:102px;top:50px">05</div>
    <h3 class="abs step-title" style="left:102px;top:93px">Submit your PIN</h3>
    <p class="abs step-body" style="left:102px;top:125px;width:250px">To submit your PIN use the text message (for example): PIN= <em>12345678</em><br>or just text the pin number: <em>12345678</em></p>
    <div class="phone" style="left:370px;top:48px;height:218px">
      <div class="phone__status"><span class="phone__time">15:12</span><span class="phone__signal">LTE ▮</span></div>
      <div class="phone__head"><span>‹</span><span>(555) 010-4471</span><span>☏ ⋯</span></div>
      <div class="msg" style="margin-top:2px"><span class="msg__avatar"></span><div class="msg__text">create a new account. Please send your PIN to complete your transaction.<div class="msg__meta">(555) 010-4471 · 15:12</div></div></div>
      <div class="sent"><span class="link">12345678</span><small>15:12</small></div>
      <div class="msg"><span class="msg__avatar" style="visibility:hidden"></span><div class="msg__text"><span class="link">+15203318867</span> will be notified when their account has been created</div></div>
      <div class="msg"><span class="msg__avatar"></span><div class="msg__text">You have received a payment of TOKAS, amount: 10 from PelloMark.<div class="msg__meta">(555) 010-4471 · 15:12</div></div></div>
      <div class="phone__input">▢ ▣ |Type a message</div>
      <div class="keys"><span>Q</span><span>W</span><span>E</span><span>R</span><span>T</span><span>Y</span><span>U</span><span>I</span><span>O</span><span>P</span></div>
      <div class="keys"><span>A</span><span>S</span><span>D</span><span>F</span><span>G</span><span>H</span><span>J</span><span>K</span><span>L</span></div>
    </div>
  </div>

  <div class="abs section tinted" style="top:776px;height:245px">
    <div class="phone" style="left:82px;top:29px;height:216px">
      <div class="phone__status"><span class="phone__time">15:20</span><span class="phone__signal">LTE ▮</span></div>
      <div class="phone__head"><span>‹</span><span>(555) 010-4471</span><span>☏ ⋯</span></div>
      <div class="sent" style="margin-top:2px">Help change pin<small>15:18</small></div>
      <div class="msg"><span class="msg__avatar"></span><div class="msg__text">To change your pin use the text message (for example): change pin to <span class="link">12345678</span><div class="msg__meta">(555) 010-4471 · 15:18</div></div></div>
      <div class="sent">Help refer<small>15:20</small></div>
      <div class="msg"><span class="msg__avatar"></span><div class="msg__text">To refer a prospective user to PelloMark send the text message (for example): refer <span class="link">+1234567890</span><div class="msg__meta">(555) 010-4471 · 15:20</div></div></div>
      <div class="phone__input">▢ ▣ Type a message</div>
      <div class="keys"><span>Q</span><span>W</span><span>E</span><span>R</span><span>T</span><span>Y</span><span>U</span><span>I</span><span>O</span><span>P</span></div>
      <div class="keys"><span>A</span><span>S</span><span>D</span><span>F</span><span>G</span><span>H</span><span>J</span><span>K</span><span>L</span></div>
    </div>
    <div class="abs step-num" style="left:273px;top:34px">06</div>
    <h3 class="abs step-title" style="left:273px;top:76px">Refer a new user</h3>
    <p class="abs step-body" style="left:273px;top:108px;width:250px">To refer a new user to PelloMark,<br>send the text message (for example):<br>refer <em>+1234567890</em></p>
  </div>

  <div class="abs section plain" style="top:1021px;height:267px">
    <div class="abs step-num" style="left:102px;top:52px">07</div>
    <h3 class="abs step-title" style="left:102px;top:94px;width:240px">To receive help from PelloMark</h3>
    <p class="abs step-body" style="left:102px;top:146px;width:262px">Help is available on all PelloMark commands by sending text messages such as:<br><em>help send</em>, or: <em>help help</em></p>
    <div class="phone" style="left:370px;top:49px;height:218px">
      <div class="phone__status"><span class="phone__time">15:16</span><span class="phone__signal">LTE ▮</span></div>
      <div class="phone__head"><span>‹</span><span>(555) 010-4471</span><span>☏ ⋯</span></div>
      <div class="msg" style="margin-top:2px"><span class="msg__avatar"></span><div class="msg__text">multiple currency denominations. Your balances are:<br>&nbsp;TOKAS &nbsp; 14<div class="msg__meta">(555) 010-4471 · 15:15</div></div></div>
      <div class="sent">Help<small>15:16</small></div>
      <div class="msg"><span class="msg__avatar"></span><div class="msg__text">Thank you for using PelloMark. For help, send "help &lt;command&gt;", where &lt;command&gt; is one of [start, stop, send, create, change (your PIN), balances, refer].<div class="msg__meta">(555) 010-4471 · 15:16</div></div></div>
      <div class="phone__input">▢ ▣ Type a message</div>
      <div class="keys"><span>Q</span><span>W</span><span>E</span><span>R</span><span>T</span><span>Y</span><span>U</span><span>I</span><span>O</span><span>P</span></div>
      <div class="keys"><span>A</span><span>S</span><span>D</span><span>F</span><span>G</span><span>H</span><span>J</span><span>K</span><span>L</span></div>
    </div>
  </div>

  <div class="abs section cta">
    <p class="abs center" style="top:40px;font-size:20px;font-weight:700;color:#fff;letter-spacing:.4px">Open your free bank account</p>
    <div class="abs cta__btn">pellomark.example/register</div>
  </div>

  <footer class="abs section footer">
    <div class="placeholder" role="img" aria-label="Faint dotted world map" style="left:145px;top:5px;width:310px;height:135px;border-radius:40px;background:radial-gradient(ellipse at center,#eef0f4,#ffffff 75%)"></div>
    <div class="abs center" style="top:25px;display:flex;justify-content:center"><div class="brand" style="font-size:19px;gap:8px"><span class="brand__dot" style="width:32px;height:32px"></span>PelloMark</div></div>
    <div class="abs center" style="top:73px;display:flex;justify-content:center;gap:9px"><span class="social"></span><span class="social"></span><span class="social"></span><span class="social"></span></div>
    <div class="abs center footnav" style="top:106px"><span>Home</span><span>About us</span><span>Contact us</span><span>Unit</span><span>Debit Card</span><span>Rewards</span><span>Store</span><span>Education</span><span>Login</span></div>
  </footer>

  <div class="abs section copyright">
    <p class="abs center" style="top:19px;font-size:6.5px;color:#444">© Copyright 2021 All Rights Reserved</p>
    <div class="abs" style="left:502px;top:15px;width:18px;height:18px;background:var(--navy);color:#fff;font-size:8px;text-align:center;line-height:18px">⌃</div>
  </div>
</section>

</body>
</html>
```